Web Design Project

8 page static website.
About us/What we stand for:
Forno Verde CBD plans to make a huge splash in Sydney by being the first Italian pizza and pasta retail food outlet offering truly fresh, nutritious ingredients – herbs and vegetables are picked directly from the garden, pizzas are made with love in a fun filled atmosphere and a cutting edge brand strategy that promotes a happy lifestyle and reminds people that happiness and togetherness comes from sharing amazing food.
The best thing about Forno Verde is that it offers consumers a choice to either choose from the enticing gluten free and vegetarian menu range to the more traditional pizza and pasta, we cater for their own tastes, this provides a distinct point of difference in the retail food market, as well as allowing consumers to have an endless range of choices without having to worry about the nutritional value.
Consumers have now become accustomed to a consistent brand experience which is setting increasingly high standards when it comes to food quality, taste and service.
We want to capitalise on the opportunity to create a strong, modern brand that promotes healthy lifestyle habits, sells fresh, wholesome ingredients, delivers
exceptional service in a fun filled atmosphere and appeals to a broad market.
Our business model is specifically pickup and delivery with a few seats and crates for eating in. It is for the time poor that still want to have a great tasting Italian experience with pizza and pasta within the quick service restaurant space. Takeaway, office catering and delivery will be a large percentage of our business.
Our philosophy at Forno Verde is simple:
“Success is not a formula, it’s a recipe”.
Brand personality:
We are located in a laneway and basically the shop is a hole in the one. It looks like a restaurant you would see in Italy.
Modern Italian, contemporary, fun, rustic (Taco Rondo, Brasa’t)
1 Aims of this website
• Emotionally connect with the target audience to reflect (“happiness and togetherness comes from sharing amazing food”)
• To entice people to order pizza
• To capture a mailing list
• To differentiate us from the low cost, low quality pizza
• To create a connection with the target audience, and promote word of mouth
2 Target audience(s)
• Male/Female
• 18-49
• Sydney CBD and Pemberly Quay
• Internet Savvy.
3. Contents/Functionality
www.crustwagon.com.au – like the rustic brown in the website and the old washed out white colour through the font.
Target Market(s)
18-49 years old
City worker and resident
people that enjoy good food
Industry/Entity Type
Restaurant
Requirements
Must have
- Some splash of red and green to represent the italian theme.
Attached is a draft of the homepage layout.
Attached below are some fonts that we like.
Nice to have
- Please see http://www.brasat.com.au/Pages/locationmenu.aspx
This is how our takeaway menu looks like.

```html
<!DOCTYPE html>
<html lang="en">
<head>
<meta charset="utf-8">
<title>Forno Verde</title>
<link rel="stylesheet" href="https://fonts.googleapis.com/css2?family=Arimo:wght@400;700&family=Quattrocento:wght@700&family=Rosario:wght@400;500&display=swap">
<style>
:root{
  --green-deep:#0f260b;
  --green-mid:#234a1a;
  --green-light:#3a6a2a;
  --red:#a50f0f;
  --red-dark:#7d0a0a;
  --tab-green:#4c9a3a;
  --parchment:#e2c48c;
  --parchment-dark:#b98a4d;
  --ink-red:#8b1a10;
  --ink-green:#2b3a1a;
  --gold:#e3b44a;
  --white:#ffffff;
  --sans:"Rosario",sans-serif;
  --serif:"Quattrocento",serif;
  --body:"Arimo",sans-serif;
}
*{margin:0;padding:0;box-sizing:border-box}
html,body{width:928px;height:1200px;overflow:hidden}
body{position:relative;background:var(--green-deep);font-family:var(--body);color:var(--white)}
.abs{position:absolute}
.header{left:0;top:0;width:928px;height:232px;background:radial-gradient(ellipse at 45% 30%,var(--green-light),var(--green-mid) 60%,#17340f)}
.logo-card{left:32px;top:32px;width:244px;height:162px}
.logo-name{left:32px;top:96px;width:244px;text-align:center;font-family:var(--sans);font-weight:500;font-size:26px;color:var(--red)}
.social{top:38px;width:30px;height:30px;border-radius:5px;background:linear-gradient(#6fa0d8,#2c5e9e)}
.order-btn{left:737px;top:93px;width:146px;height:37px;border-radius:18px;background:linear-gradient(#e0404a,#a80f18);color:var(--white);font-family:var(--body);font-weight:700;font-size:19px;line-height:37px;text-align:center;box-shadow:0 2px 3px rgba(0,0,0,.5)}
.nav{left:298px;top:156px;width:617px;height:49px;background:linear-gradient(var(--red),var(--red-dark));border-radius:3px}
.nav-tab{left:323px;top:147px;width:81px;height:55px;background:var(--tab-green)}
.nav-item{top:170px;font-family:var(--serif);font-size:16px;font-weight:700;color:var(--white);transform:translateX(-50%);letter-spacing:.3px}
.banner{left:5px;top:232px;width:915px;height:398px;background:radial-gradient(ellipse at 60% 50%,var(--parchment),var(--parchment-dark))}
.banner-photo{left:26px;top:262px;width:584px;height:344px;border:3px solid var(--white);border-radius:8px;background:radial-gradient(circle at 40% 45%,#6a7a2a,#5a3418 55%,#3a2010)}
.stamp{left:670px;top:263px;width:166px;height:59px;border:3px solid var(--ink-red);font-family:var(--serif);font-weight:700;font-size:21px;line-height:24px;color:var(--ink-red);text-align:center;padding-top:4px}
.tagline{left:610px;top:354px;width:286px;text-align:center;font-family:var(--sans);font-size:24px;line-height:36px;color:var(--ink-green)}
.intro{left:610px;top:434px;width:286px;text-align:center;font-family:var(--sans);font-size:17px;line-height:28px;color:var(--ink-red)}
.dot{top:579px;width:18px;height:18px;border-radius:50%;background:#1a1a1a}
.dot.active{background:#8b0000}
.card{top:672px;width:218px;height:168px;border-radius:4px;background:linear-gradient(#c59a5c,#f2dca8)}
.card-photo{background:linear-gradient(#d7d2c8,#8a7c68)}
.card-title{font-family:var(--sans);font-size:20px;line-height:35px;color:var(--ink-red)}
.email-title{left:239px;top:684px;width:218px;text-align:center;font-family:var(--sans);font-weight:500;font-size:18px;color:var(--ink-red)}
.label{font-family:var(--body);font-size:12px;font-weight:700;color:#222}
.input{left:296px;width:136px;height:21px;background:var(--white);border:1px solid #999}
.submit{left:300px;top:802px;width:87px;height:28px;border-radius:5px;background:linear-gradient(#c01010,#8a0808);font-family:var(--sans);font-weight:500;font-size:14px;line-height:28px;text-align:center}
.section-title{left:60px;top:878px;font-family:var(--sans);font-size:24px;color:#e6e6e6}
.avatar{top:945px;width:76px;height:76px;border:3px solid var(--white);background:linear-gradient(#e8e4dc,#a89682)}
.quote{top:936px;width:175px;font-size:11px;line-height:17px;color:#f2f2f2}
.quote-mark{font-family:var(--serif);font-size:18px;line-height:0}
.author{top:1026px;font-size:13px;color:var(--gold)}
.divider{top:918px;height:150px;border-left:1px dotted #5a6a50}
.footer{left:0;top:1100px;width:928px;height:100px;background:radial-gradient(ellipse at 50% 0%,var(--green-light),var(--green-mid) 55%,#17340f)}
.footer-nav{left:0;top:1118px;width:928px;text-align:center;font-size:11px;color:var(--white)}
.footer-nav span{margin:0 6px}
.copyright{left:0;top:1152px;width:928px;text-align:center;font-size:11px;color:var(--white)}
</style>
</head>
<body>
<header class="abs header"></header>
<svg class="abs logo-card" viewBox="0 0 244 162" aria-hidden="true">
  <path d="M4 8 Q122 -4 232 6 L242 156 Q130 140 14 158 Z" fill="#fff" stroke="#ddd" stroke-width="2"/>
</svg>
<div class="abs logo-name">Forno Verde</div>

<div class="abs social" style="left:750px"></div>
<div class="abs social" style="left:784px"></div>
<div class="abs social" style="left:818px"></div>
<div class="abs social" style="left:852px;background:linear-gradient(#f8a040,#e06a10)"></div>
<div class="abs order-btn">ORDER NOW</div>

<nav>
  <div class="abs nav"></div>
  <div class="abs nav-tab"></div>
  <div class="abs nav-item" style="left:362px">HOME</div>
  <div class="abs nav-item" style="left:511px">ABOUT US</div>
  <div class="abs nav-item" style="left:660px">MENU</div>
  <div class="abs nav-item" style="left:819px">CONTACT US</div>
</nav>

<section class="abs banner"></section>
<div class="abs banner-photo" role="img" aria-label="Close-up of a pizza topped with fresh coriander and banana peppers"></div>
<div class="abs stamp">FORNO<br>VERDE</div>
<div class="abs tagline">Success is not a formula,<br>it’s a recipe</div>
<div class="abs intro">Lorem ipsum dolor sit amet,<br>consectetuer adipiscing elit.<br>Lorem ipsum dolor sit amet,<br>adipiscing elit</div>
<div class="abs dot active" style="left:724px"></div>
<div class="abs dot" style="left:743px"></div>
<div class="abs dot" style="left:763px"></div>
<div class="abs dot" style="left:782px"></div>

<section>
  <div class="abs card" style="left:7px"></div>
  <div class="abs card-photo" style="left:15px;top:679px;width:145px;height:154px" role="img" aria-label="Woman ordering on a laptop"></div>
  <div class="abs card-title" style="left:100px;top:736px">Click here to<br>Order Online</div>

  <div class="abs card" style="left:239px"></div>
  <div class="abs email-title">Join Our Email Club</div>
  <div class="abs label" style="left:252px;top:735px">Name :</div>
  <div class="abs input" style="top:731px"></div>
  <div class="abs label" style="left:252px;top:773px">Email :</div>
  <div class="abs input" style="top:769px"></div>
  <div class="abs submit">Submit</div>

  <div class="abs card" style="left:471px"></div>
  <div class="abs card-photo" style="left:477px;top:679px;width:144px;height:154px;background:linear-gradient(#a09070,#6a4a30)" role="img" aria-label="Guests serving themselves at a catered office buffet"></div>
  <div class="abs card-title" style="left:620px;top:723px">Office<br>Catering</div>

  <div class="abs card" style="left:703px"></div>
  <div class="abs card-photo" style="left:712px;top:673px;width:96px;height:167px;background:linear-gradient(#c0302a,#2a3a5a)" role="img" aria-label="Delivery driver carrying a pizza bag"></div>
  <div class="abs card-title" style="left:797px;top:736px">Delivery Area</div>
</section>

<section>
  <svg class="abs" style="left:25px;top:883px" width="26" height="24" viewBox="0 0 26 24" aria-hidden="true">
    <path d="M2 2 H24 V17 H12 L7 22 V17 H2 Z" fill="#e6e6e6"/>
  </svg>
  <h2 class="abs section-title" style="font-weight:400">Testimonials</h2>

  <div class="abs avatar" style="left:24px" role="img" aria-label="Customer portrait"></div>
  <p class="abs quote" style="left:127px"><span class="quote-mark">“</span><br>&nbsp;&nbsp;Thanks so much for a superb meal on Saturday. It quite made the evening for Marco and I to have you in the kitchen.<span class="quote-mark">”</span></p>
  <div class="abs author" style="left:127px">Marco and Giulia Bennett</div>
  <div class="abs divider" style="left:311px"></div>

  <div class="abs avatar" style="left:337px" role="img" aria-label="Customer portrait"></div>
  <p class="abs quote" style="left:440px"><span class="quote-mark">“</span><br>&nbsp;&nbsp;Thanks so much for a superb meal on Saturday. It quite made the evening for Marco and I to have you in the kitchen.<span class="quote-mark">”</span></p>
  <div class="abs author" style="left:440px">Marco and Giulia Bennett</div>
  <div class="abs divider" style="left:627px"></div>

  <div class="abs avatar" style="left:649px" role="img" aria-label="Customer portrait"></div>
  <p class="abs quote" style="left:752px"><span class="quote-mark">“</span><br>&nbsp;&nbsp;Thanks so much for a superb meal on Saturday. It quite made the evening for Marco and I to have you in the kitchen.<span class="quote-mark">”</span></p>
  <div class="abs author" style="left:752px">Marco and Giulia Bennett</div>
</section>

<footer class="abs footer"></footer>
<div class="abs footer-nav">Home<span>|</span>About Us<span>|</span>Menu<span>|</span>Contact Us</div>
<div class="abs copyright">Copyright © FornoVerde,All Rights Reserved</div>
</body>
</html>
```